simple, clean, smart design for PPT template!

We need a template design for ouw company Brenthollow. Please refer to the business cad design and our web site.

Our message is Wisdome and Knowledge, and the image is "simple" and "clean".
http://www.brenthollow.example/

You may want to refer to the company like KDT, Solvarine, RMN, Tyvor, etc.

Target Market(s)

Every business industry.

Industry/Entity Type

Consulting

Font styles to use
Other font styles liked:
• Please refer to your sense from our corporate image.

Requirements
Must have
• company logo. the colors should be limited to ones used for the logo. The final version of your file must be submitted in PPT format.
Nice to have
• The corporate image is always "simple and clean".
Should not have
• No pictures of human face.

```html
<!DOCTYPE html>
<html lang="en">
<head>
<meta charset="utf-8">
<title>Brenthollow — Business Proposal Template</title>
<link href="https://fonts.googleapis.com/css2?family=Open+Sans:wght@400;600;700;800&display=swap" rel="stylesheet">
<style>
:root{
  --stage:#121212;
  --green:#8cc63f;
  --green-soft:#b7db85;
  --dark:#4a4a4a;
  --ink:#333333;
  --muted:#9a9a9a;
  --faint:#c4c4c4;
  --rule:#e6e6e6;
  --white:#ffffff;
}
*{margin:0;padding:0;box-sizing:border-box}
html,body{width:1200px;height:1200px;overflow:hidden;background:var(--stage)}
body{position:relative;font-family:"Open Sans",Arial,sans-serif}
.slide{position:absolute;background:var(--white);overflow:hidden}
.slide svg{display:block;width:100%;height:100%}
text{font-family:"Open Sans",Arial,sans-serif}
.logo{font-size:7px;font-weight:600;fill:var(--green)}
.sub{font-size:4.2px;fill:var(--muted);text-anchor:middle}
.ttl{font-size:9.5px;fill:var(--ink);font-weight:600;text-anchor:middle}
.lbl{font-size:4.2px;font-weight:700;fill:var(--ink)}
.tiny{font-size:3.2px;fill:var(--muted)}
.foot{font-size:3px;fill:var(--faint)}
.mid{text-anchor:middle}
.end{text-anchor:end}
.hl-green{font-size:6px;font-weight:600;fill:var(--green)}
.hl-dark{font-size:6px;font-weight:700;fill:var(--ink)}
.hl-gray{font-size:6px;font-weight:600;fill:var(--faint)}
.year{font-size:3.2px;fill:var(--faint)}
.dot{fill:var(--green)}
.node-txt{font-size:3.2px;fill:#fff;text-anchor:middle}
.hero{font-weight:800;fill:#fff}
.white-small{font-size:4px;fill:rgba(255,255,255,.8)}
</style>
</head>
<body>

<!-- 1 Cover -->
<div class="slide" style="left:114px;top:14px;width:291px;height:164px">
<svg viewBox="0 0 291 164">
  <defs><linearGradient id="g-cover" x1="0" y1="0" x2="1" y2="1"><stop offset="0" stop-color="#3a4656"/><stop offset="1" stop-color="#2a3340"/></linearGradient></defs>
  <rect width="291" height="164" fill="url(#g-cover)" role="img" aria-label="Team meeting around a wooden table, seen from above"/>
  <text x="146" y="75" class="hero mid" style="font-size:19px">BUSINESS</text>
  <text x="146" y="96" class="hero mid" style="font-size:19px">PROPOSAL</text>
  <text x="146" y="106" class="white-small mid">Creative Presentation Template</text>
  <text x="146" y="140" class="white-small mid" style="font-size:3px">Presented by You</text>
</svg></div>

<!-- 2 Content overview -->
<div class="slide" style="left:440px;top:14px;width:298px;height:164px">
<svg viewBox="0 0 298 164">
  <circle cx="13" cy="16" r="3.5" class="dot"/><text x="19" y="18.5" class="logo">Brenthollow</text>
  <circle cx="274" cy="15" r="4" class="dot"/>
  <text x="149" y="13" class="sub">Insert your subtitle text here</text>
  <text x="149" y="26" class="ttl">Presentation Content Overview</text>
  <rect x="143" y="30" width="12" height="1" fill="var(--ink)"/>
  <circle cx="133" cy="48" r="2.5" class="dot"/><text x="137" y="50" class="logo" style="font-size:5px">Brenthollow</text>
  <line x1="58" y1="84" x2="298" y2="84" stroke="var(--green-soft)" stroke-width=".8"/>
  <circle cx="41" cy="84" r="18" fill="#fff" stroke="#e8f2da" stroke-width="1"/>
  <path d="M35 86 L41 80 L47 86 M37 85 V90 H45 V85" fill="none" stroke="var(--green)" stroke-width="1"/>
  <circle cx="124" cy="84" r="7" class="dot"/><text x="124" y="83" class="node-txt">9:00</text><text x="124" y="87" class="node-txt">AM</text>
  <circle cx="210" cy="84" r="7" class="dot"/><text x="210" y="83" class="node-txt">9:15</text><text x="210" y="87" class="node-txt">AM</text>
  <text x="124" y="102" class="lbl mid">WELCOME MESSAGE</text>
  <text x="124" y="109" class="tiny mid">Tools that allow people or</text><text x="124" y="114" class="tiny mid">companies to create, share</text>
  <text x="210" y="102" class="lbl mid">ABOUT US</text>
  <text x="210" y="109" class="tiny mid">Tools that allow people or</text><text x="210" y="114" class="tiny mid">companies to create, share</text>
  <text x="20" y="157" class="foot">Business Presentation</text>
</svg></div>

<!-- 3 Overview continued -->
<div class="slide" style="left:778px;top:14px;width:302px;height:164px">
<svg viewBox="0 0 302 164">
  <circle cx="13" cy="16" r="3.5" class="dot"/><text x="19" y="18.5" class="logo">Brenthollow</text>
  <circle cx="276" cy="15" r="4" class="dot"/>
  <line x1="0" y1="84" x2="302" y2="84" stroke="var(--green-soft)" stroke-width=".8"/>
  <circle cx="46" cy="84" r="7" class="dot"/><text x="46" y="83" class="node-txt">9:30</text><text x="46" y="87" class="node-txt">AM</text>
  <circle cx="146" cy="84" r="7" fill="var(--dark)"/><text x="146" y="83" class="node-txt">10:00</text><text x="146" y="87" class="node-txt">AM</text>
  <circle cx="250" cy="84" r="7" class="dot"/><text x="250" y="83" class="node-txt">11:00</text><text x="250" y="87" class="node-txt">AM</text>
  <text x="46" y="102" class="lbl mid">OUR SERVICES</text><text x="46" y="109" class="tiny mid">Tools that allow people or</text><text x="46" y="114" class="tiny mid">companies to create, share</text>
  <text x="146" y="102" class="lbl mid">OUR SOLUTIONS</text><text x="146" y="109" class="tiny mid">Tools that allow people or</text><text x="146" y="114" class="tiny mid">companies to create, share</text>
  <text x="250" y="102" class="lbl mid">THE PROBLEM</text><text x="250" y="109" class="tiny mid">Tools that allow people or</text><text x="250" y="114" class="tiny mid">companies to create, share</text>
  <text x="20" y="157" class="foot">Business Presentation</text>
</svg></div>

<!-- 4 Overview finish -->
<div class="slide" style="left:114px;top:204px;width:294px;height:168px">
<svg viewBox="0 0 294 168">
  <circle cx="13" cy="16" r="3.5" class="dot"/><text x="19" y="18.5" class="logo">Brenthollow</text>
  <circle cx="270" cy="13" r="4" class="dot"/>
  <line x1="0" y1="82" x2="200" y2="82" stroke="var(--green-soft)" stroke-width=".8"/>
  <circle cx="46" cy="82" r="7" class="dot"/><text x="46" y="81" class="node-txt">12:30</text><text x="46" y="85" class="node-txt">PM</text>
  <circle cx="142" cy="82" r="7" fill="var(--dark)"/><text x="142" y="81" class="node-txt">01:00</text><text x="142" y="85" class="node-txt">PM</text>
  <circle cx="222" cy="82" r="22" fill="#fff" stroke="#e8f2da" stroke-width="1"/><text x="222" y="84" class="lbl mid">FINISH</text>
  <text x="46" y="101" class="lbl mid">MEET THE TEAM</text><text x="46" y="108" class="tiny mid">Tools that allow people or</text><text x="46" y="113" class="tiny mid">companies to create, share</text>
  <text x="142" y="101" class="lbl mid">OUR WORKS</text><text x="142" y="108" class="tiny mid">Tools that allow people or</text><text x="142" y="113" class="tiny mid">companies to create, share</text>
  <text x="20" y="160" class="foot">Business Presentation</text>
</svg></div>

<!-- 5 Our team / business -->
<div class="slide" style="left:440px;top:204px;width:300px;height:168px">
<svg viewBox="0 0 300 168">
  <rect x="0" y="0" width="150" height="84" fill="#e9e6e2" role="img" aria-label="Portrait of a team member"/>
  <rect x="150" y="84" width="150" height="84" fill="#7a6248" role="img" aria-label="Colleagues working at a table, seen from above"/>
  <circle cx="283" cy="13" r="4" class="dot"/>
  <text x="160" y="19" class="lbl">Our Team</text><text x="160" y="24" class="tiny" style="fill:var(--green)">Your headline here</text>
  <text x="160" y="33" class="tiny">Mobile social media refers to the combination of mobile</text>
  <text x="160" y="38" class="tiny">devices and social media. This is the group of mobile</text>
  <text x="160" y="43" class="tiny">marketing applications that allow the creation.</text>
  <text x="160" y="54" class="tiny">Due to the fact that mobile social media run on mobile</text>
  <text x="160" y="59" class="tiny">devices, it differs from traditional social media.</text>
  <text x="140" y="97" class="lbl end">Our Business</text><text x="140" y="102" class="tiny end" style="fill:var(--green)">Your headline here</text>
  <text x="140" y="111" class="tiny end">Mobile social media refers to the combination of mobile</text>
  <text x="140" y="116" class="tiny end">devices and social media. This is the group of mobile</text>
  <text x="140" y="121" class="tiny end">marketing applications that allow the creation.</text>
  <text x="140" y="132" class="tiny end">Due to the fact that mobile social media run on mobile</text>
  <text x="140" y="137" class="tiny end">devices, it differs from traditional social media.</text>
  <text x="20" y="161" class="foot">Business Presentation</text>
</svg></div>

<!-- 6 History through time -->
<div class="slide" style="left:778px;top:204px;width:308px;height:168px">
<svg viewBox="0 0 308 168">
  <circle cx="13" cy="16" r="3.5" class="dot"/><text x="19" y="18.5" class="logo">Brenthollow</text>
  <circle cx="282" cy="13" r="4" class="dot"/>
  <text x="154" y="13" class="sub">Insert your subtitle text here</text>
  <text x="154" y="26" class="ttl">Our History Through The Time</text>
  <line x1="154" y1="44" x2="154" y2="168" stroke="var(--green-soft)" stroke-width=".8" stroke-dasharray="2 2"/>
  <circle cx="154" cy="47" r="1.8" class="dot"/><circle cx="154" cy="68" r="1.8" class="dot"/><circle cx="154" cy="96" r="1.8" class="dot"/><circle cx="154" cy="124" r="1.8" class="dot"/><circle cx="154" cy="148" r="1.8" class="dot"/>
  <text x="136" y="48" class="hl-green end">FUNDATION</text><text x="136" y="54" class="year end">1980</text>
  <text x="136" y="97" class="hl-dark end">BIG CONTRACT</text><text x="136" y="103" class="year end">2000</text>
  <text x="136" y="149" class="hl-gray end">COUNTRIES</text><text x="136" y="155" class="year end">2010</text>
  <text x="170" y="69" class="hl-green">OPENED NEW</text><text x="170" y="76" class="hl-green">LOCATIONS</text><text x="170" y="82" class="year">1990</text>
  <text x="170" y="125" class="hl-green">NEW MEMBERS</text><text x="170" y="131" class="year">2005</text>
  <text x="20" y="161" class="foot">Business Presentation</text>
</svg></div>

<!-- 7 Milestones -->
<div class="slide" style="left:114px;top:397px;width:298px;height:168px">
<svg viewBox="0 0 298 168">
  <circle cx="13" cy="16" r="3.5" class="dot"/><text x="19" y="18.5" class="logo">Brenthollow</text>
  <circle cx="274" cy="13" r="4" class="dot"/>
  <line x1="150" y1="8" x2="150" y2="168" stroke="var(--green-soft)" stroke-width=".8" stroke-dasharray="2 2"/>
  <circle cx="150" cy="14" r="1.8" class="dot"/><circle cx="150" cy="35" r="1.8" class="dot"/><circle cx="150" cy="61" r="1.8" class="dot"/><circle cx="150" cy="89" r="1.8" class="dot"/><circle cx="150" cy="111" r="1.8" class="dot"/>
  <text x="134" y="15" class="hl-green end">NEW LOCATIONS</text><text x="134" y="21" class="year end">2011</text>
  <text x="134" y="62" class="hl-dark end">100K SALES</text><text x="134" y="68" class="year end">2015</text>
  <text x="134" y="112" class="hl-gray end">LIVE NOW</text><text x="134" y="118" class="year end">2020</text>
  <text x="166" y="36" class="hl-green">1,000,000</text><text x="166" y="43" class="hl-green">MEMBERS</text><text x="166" y="49" class="year">2013</text>
  <text x="166" y="90" class="hl-green">NEW STORE</text><text x="166" y="96" class="year">2019</text>
  <text x="20" y="161" class="foot">Business Presentation</text>
</svg></div>

<!-- 8 Company profile -->
<div class="slide" style="left:440px;top:397px;width:304px;height:168px">
<svg viewBox="0 0 304 168">
  <rect width="304" height="168" fill="#7c6a54" role="img" aria-label="Business meeting on a wooden desk, seen from above"/>
  <circle cx="240" cy="88" r="96" fill="var(--green)" opacity=".92"/>
  <line x1="205" y1="42" x2="282" y2="42" stroke="rgba(255,255,255,.6)" stroke-width=".6"/>
  <text x="282" y="71" class="hero end" style="font-size:18px">COMPANY</text>
  <text x="282" y="92" class="hero end" style="font-size:18px">PROFILE</text>
  <text x="282" y="104" class="white-small end">Your great headline text here</text>
  <line x1="205" y1="125" x2="282" y2="125" stroke="rgba(255,255,255,.6)" stroke-width=".6"/>
</svg></div>

<!-- 9 Message from CEO -->
<div class="slide" style="left:778px;top:397px;width:311px;height:175px">
<svg viewBox="0 0 311 175">
  <circle cx="13" cy="16" r="3.5" class="dot"/><text x="19" y="18.5" class="logo">Brenthollow</text>
  <circle cx="285" cy="13" r="4" class="dot"/>
  <text x="156" y="13" class="sub">Insert your subtitle text here</text>
  <text x="156" y="26" class="ttl">Message From Our CEO</text>
  <rect x="150" y="30" width="12" height="1" fill="var(--green)"/>
  <rect x="0" y="50" width="311" height="89" fill="#5b6470" role="img" aria-label="Office interior with a colleague at a desk"/>
  <text x="30" y="80" style="font-size:5px;font-weight:600;fill:#fff">HAPPY CUSTOMERS</text>
  <text x="30" y="92" class="white-small">"Mobile social media refers to the combination of</text>
  <text x="30" y="99" class="white-small">mobile devices and social media. This is a group</text>
  <text x="30" y="106" class="white-small">of mobile marketing applications"</text>
  <text x="288" y="88" class="hero end" style="font-size:14px">Our</text>
  <text x="288" y="104" class="hero end" style="font-size:14px">Top Priority</text>
  <text x="22" y="167" class="foot">Business Presentation</text>
</svg></div>

<!-- 10 Our mission -->
<div class="slide" style="left:114px;top:592px;width:300px;height:170px">
<svg viewBox="0 0 300 170">
  <rect width="300" height="170" fill="#d9d9d9" role="img" aria-label="People seated in a row during a meeting"/>
  <path d="M192 0 H300 V170 H184 Z" fill="var(--green)" opacity=".88"/>
  <text x="278" y="43" class="hero end" style="font-size:13px">Our</text>
  <text x="278" y="58" class="hero end" style="font-size:13px">Mission</text>
  <text x="278" y="80" class="white-small end">Mobile social media refers to</text>
  <text x="278" y="87" class="white-small end">the combination of mobile</text>
  <text x="278" y="94" class="white-small end">devices and social media.</text>
  <text x="278" y="101" class="white-small end">This is a group of mobile</text>
  <text x="278" y="108" class="white-small end">marketing applications that</text>
  <text x="278" y="115" class="white-small end">allow the creation and</text>
  <text x="278" y="122" class="white-small end">exchange of user.</text>
  <text x="278" y="140" class="white-small end">Jon Pellard</text>
</svg></div>

<!-- 11 History from the beginning -->
<div class="slide" style="left:440px;top:592px;width:309px;height:174px">
<svg viewBox="0 0 309 174">
  <circle cx="13" cy="16" r="3.5" class="dot"/><text x="19" y="18.5" class="logo">Brenthollow</text>
  <circle cx="283" cy="13" r="4" class="dot"/>
  <text x="154" y="13" class="sub">Insert your subtitle text here</text>
  <text x="154" y="26" class="ttl">Our History From The Beginning</text>
  <rect x="148" y="30" width="12" height="1" fill="var(--ink)"/>
  <g fill="none" stroke="#cfd8c4" stroke-width=".8">
    <circle cx="51" cy="51" r="7"/><circle cx="134" cy="51" r="7" stroke="var(--dark)"/><circle cx="218" cy="51" r="7"/>
    <circle cx="91" cy="134" r="7"/><circle cx="175" cy="134" r="7"/><circle cx="260" cy="134" r="7"/>
  </g>
  <g stroke="#dcdcdc" stroke-width=".6">
    <line x1="51" y1="60" x2="51" y2="84"/><line x1="134" y1="60" x2="134" y2="84"/><line x1="218" y1="60" x2="218" y2="84"/>
    <line x1="91" y1="102" x2="91" y2="125"/><line x1="175" y1="102" x2="175" y2="125"/><line x1="260" y1="102" x2="260" y2="125"/>
  </g>
  <rect x="30" y="91" width="40" height="4" fill="var(--green)"/>
  <rect x="71" y="91" width="40" height="4" fill="var(--green)"/>
  <rect x="112" y="91" width="41" height="4" fill="var(--dark)"/>
  <rect x="154" y="91" width="41" height="4" fill="var(--green)"/>
  <rect x="196" y="91" width="41" height="4" fill="#c7cfd8"/>
  <rect x="238" y="91" width="42" height="4" fill="var(--green)"/>
  <text x="92" y="51" class="lbl mid">1994</text><text x="92" y="58" class="tiny mid">Tools that allow people or</text><text x="92" y="63" class="tiny mid">companies to create, share</text>
  <text x="176" y="51" class="lbl mid">2002</text><text x="176" y="58" class="tiny mid">Tools that allow people or</text><text x="176" y="63" class="tiny mid">companies to create, share</text>
  <text x="260" y="51" class="lbl mid">2016</text><text x="260" y="58" class="tiny mid">Tools that allow people or</text><text x="260" y="63" class="tiny mid">companies to create, share</text>
  <text x="51" y="121" class="lbl mid">1990</text><text x="51" y="128" class="tiny mid">Tools that allow people or</text><text x="51" y="133" class="tiny mid">companies to create, share</text>
  <text x="134" y="121" class="lbl mid">1998</text><text x="134" y="128" class="tiny mid">Tools that allow people or</text><text x="134" y="133" class="tiny mid">companies to create, share</text>
  <text x="218" y="121" class="lbl mid">2007</text><text x="218" y="128" class="tiny mid">Tools that allow people or</text><text x="218" y="133" class="tiny mid">companies to create, share</text>
  <path d="M257 134 l2 2 l4 -4" fill="none" stroke="var(--green)" stroke-width=".8"/>
  <text x="22" y="166" class="foot">Business Presentation</text>
</svg></div>

<!-- 12 Our team -->
<div class="slide" style="left:778px;top:592px;width:314px;height:176px">
<svg viewBox="0 0 314 176">
  <rect width="314" height="176" fill="#c9ccd0" role="img" aria-label="Two colleagues reviewing work at a laptop"/>
  <circle cx="75" cy="88" r="88" fill="var(--green)" opacity=".95"/>
  <line x1="22" y1="44" x2="100" y2="44" stroke="rgba(255,255,255,.6)" stroke-width=".6"/>
  <text x="22" y="77" class="hero" style="font-size:19px">OUR</text>
  <text x="22" y="99" class="hero" style="font-size:19px">TEAM</text>
  <text x="22" y="110" class="white-small">Your great headline text here</text>
  <line x1="22" y1="128" x2="100" y2="128" stroke="rgba(255,255,255,.6)" stroke-width=".6"/>
</svg></div>

<!-- 13 Meet our CEO -->
<div class="slide" style="left:110px;top:782px;width:309px;height:173px">
<svg viewBox="0 0 309 173">
  <circle cx="13" cy="16" r="3.5" class="dot"/><text x="19" y="18.5" class="logo">Brenthollow</text>
  <circle cx="283" cy="13" r="4" class="dot"/>
  <text x="154" y="13" class="sub">Insert your subtitle text here</text>
  <text x="154" y="26" class="ttl">Meet Our CEO</text>
  <rect x="148" y="30" width="12" height="1" fill="var(--ink)"/>
  <rect x="29" y="60" width="59" height="60" fill="#e3e1de" role="img" aria-label="Portrait of the CEO"/>
  <text x="102" y="64" class="lbl">Kenji Marlow</text><text x="102" y="69" class="tiny" style="fill:var(--green)">CEO, Founder</text>
  <text x="102" y="78" class="tiny">Mobile social media refers to the combination</text>
  <text x="102" y="83" class="tiny">of mobile devices and social media. This is the</text>
  <text x="102" y="88" class="tiny">group of mobile marketing applications that</text>
  <text x="102" y="93" class="tiny">allow the creation and exchange of content.</text>
  <text x="102" y="104" class="tiny">Due to the fact that mobile social media run on</text>
  <text x="102" y="109" class="tiny">mobile devices.</text>
  <text x="207" y="64" class="lbl">Skills</text><text x="207" y="69" class="tiny" style="fill:var(--green)">Director General</text>
  <g class="tiny">
    <text x="207" y="84">Speaking</text><text x="207" y="93">Leadership</text><text x="207" y="102">Social Media</text><text x="207" y="111">Marketing</text>
  </g>
  <rect x="233" y="81" width="50" height="3" fill="#eee"/><rect x="233" y="81" width="37" height="3" class="dot"/>
  <rect x="233" y="90" width="50" height="3" fill="#eee"/><rect x="233" y="90" width="43" height="3" class="dot"/>
  <rect x="233" y="99" width="50" height="3" fill="#eee"/><rect x="233" y="99" width="35" height="3" fill="var(--dark)"/>
  <rect x="233" y="108" width="50" height="3" fill="#eee"/><rect x="233" y="108" width="40" height="3" fill="#c7cfd8"/>
  <text x="22" y="166" class="foot">Business Presentation</text>
</svg></div>

<!-- 14 Our team grid -->
<div class="slide" style="left:437px;top:782px;width:309px;height:173px">
<svg viewBox="0 0 309 173">
  <circle cx="13" cy="16" r="3.5" class="dot"/><text x="19" y="18.5" class="logo">Brenthollow</text>
  <circle cx="283" cy="13" r="4" class="dot"/>
  <text x="154" y="13" class="sub">Insert your subtitle text here</text>
  <text x="154" y="26" class="ttl">Our Team</text>
  <rect x="148" y="30" width="12" height="1" fill="var(--ink)"/>
  <rect x="24" y="58" width="41" height="41" fill="#e5e2de" role="img" aria-label="Portrait of Aya Renfield"/>
  <rect x="157" y="58" width="41" height="41" fill="#e5e2de" role="img" aria-label="Portrait of Emi Castell"/>
  <rect x="24" y="104" width="41" height="41" fill="#e5e2de" role="img" aria-label="Portrait of Taro Ellsby"/>
  <rect x="157" y="104" width="41" height="41" fill="#e5e2de" role="img" aria-label="Portrait of Rina Halvorsen"/>
  <text x="73" y="63" class="lbl">Aya Renfield</text><text x="73" y="68" class="tiny" style="fill:var(--green)">Director General</text>
  <text x="73" y="76" class="tiny">Mobile social media refers to the combination</text><text x="73" y="81" class="tiny">of mobile devices and social media. This is</text><text x="73" y="86" class="tiny">group of mobile marketing applications.</text>
  <text x="206" y="63" class="lbl">Emi Castell</text><text x="206" y="68" class="tiny" style="fill:var(--green)">Finance</text>
  <text x="206" y="76" class="tiny">Mobile social media refers to the combination</text><text x="206" y="81" class="tiny">of mobile devices and social media. This is</text><text x="206" y="86" class="tiny">group of mobile marketing applications.</text>
  <text x="73" y="109" class="lbl">Taro Ellsby</text><text x="73" y="114" class="tiny" style="fill:var(--green)">Managing Director</text>
  <text x="73" y="122" class="tiny">Mobile social media refers to the combination</text><text x="73" y="127" class="tiny">of mobile devices and social media. This is</text><text x="73" y="132" class="tiny">group of mobile marketing applications.</text>
  <text x="206" y="109" class="lbl">Rina Halvorsen</text><text x="206" y="114" class="tiny" style="fill:var(--green)">Branding</text>
  <text x="206" y="122" class="tiny">Mobile social media refers to the combination</text><text x="206" y="127" class="tiny">of mobile devices and social media. This is</text><text x="206" y="132" class="tiny">group of mobile marketing applications.</text>
  <text x="22" y="166" class="foot">Business Presentation</text>
</svg></div>

<!-- 15 Charts data -->
<div class="slide" style="left:775px;top:782px;width:327px;height:183px">
<svg viewBox="0 0 327 183">
  <circle cx="13" cy="16" r="3.5" class="dot"/><text x="19" y="18.5" class="logo">Brenthollow</text>
  <circle cx="300" cy="14" r="4" class="dot"/>
  <text x="164" y="13" class="sub">Insert your subtitle text here</text>
  <text x="164" y="27" class="ttl">Charts Data</text>
  <rect x="158" y="31" width="12" height="1" fill="var(--ink)"/>
  <g>
    <rect x="29" y="75" width="12" height="31" fill="var(--green-soft)"/><rect x="43" y="57" width="12" height="49" class="dot"/><rect x="57" y="80" width="12" height="26" fill="var(--dark)"/>
    <rect x="100" y="52" width="12" height="54" class="dot"/><rect x="114" y="82" width="12" height="24" fill="var(--green-soft)"/><rect x="128" y="75" width="12" height="31" fill="var(--dark)"/>
    <rect x="172" y="73" width="12" height="33" class="dot"/><rect x="186" y="65" width="12" height="41" class="dot"/><rect x="200" y="72" width="12" height="34" fill="var(--dark)"/>
    <rect x="245" y="81" width="12" height="25" fill="var(--green-soft)"/><rect x="259" y="66" width="12" height="40" class="dot"/><rect x="273" y="50" width="12" height="56" fill="var(--dark)"/>
  </g>
  <g class="tiny mid" style="font-size:2.8px">
    <text x="35" y="73">43%</text><text x="49" y="55">67%</text><text x="63" y="78">36%</text>
    <text x="106" y="50">75%</text><text x="120" y="80">34%</text><text x="134" y="73">48%</text>
    <text x="178" y="71">45%</text><text x="192" y="63">58%</text><text x="206" y="70">46%</text>
    <text x="251" y="79">34%</text><text x="265" y="64">56%</text><text x="279" y="48">89%</text>
  </g>
  <line x1="24" y1="106" x2="292" y2="106" stroke="var(--rule)" stroke-width=".5"/>
  <g class="tiny mid"><text x="49" y="112">Product 1</text><text x="120" y="112">Product 2</text><text x="192" y="112">Product 3</text><text x="265" y="112">Product 4</text></g>
  <text x="22" y="134" style="font-size:11px;fill:var(--ink);font-weight:300">01</text>
  <text x="41" y="127" class="lbl" style="font-size:3.6px">Shoes</text><text x="41" y="132" class="tiny">Tools that allow people or companies</text><text x="41" y="137" class="tiny">to create, share, or exchange info</text>
  <text x="113" y="134" style="font-size:11px;fill:var(--ink);font-weight:300">02</text>
  <text x="132" y="127" class="lbl" style="font-size:3.6px">T-Shirts</text><text x="132" y="132" class="tiny">Tools that allow people or companies</text><text x="132" y="137" class="tiny">to create, share, or exchange info</text>
  <text x="207" y="134" style="font-size:11px;fill:var(--ink);font-weight:300">03</text>
  <text x="226" y="127" class="lbl" style="font-size:3.6px">Pants</text><text x="226" y="132" class="tiny">Tools that allow people or companies</text><text x="226" y="137" class="tiny">to create, share, or exchange info</text>
  <text x="22" y="175" class="foot">Business Presentation</text>
</svg></div>

<!-- 16 Charts data driven -->
<div class="slide" style="left:107px;top:978px;width:310px;height:174px">
<svg viewBox="0 0 310 174">
  <circle cx="13" cy="16" r="3.5" class="dot"/><text x="19" y="18.5" class="logo">Brenthollow</text>
  <circle cx="284" cy="13" r="4" class="dot"/>
  <text x="155" y="13" class="sub">Insert your subtitle text here</text>
  <text x="155" y="26" class="ttl">Charts Data Driven</text>
  <rect x="149" y="30" width="12" height="1" fill="var(--ink)"/>
  <g class="tiny end"><text x="34" y="54">100%</text><text x="34" y="70">75%</text><text x="34" y="86">50%</text><text x="34" y="102">25%</text><text x="34" y="118">0%</text></g>
  <g fill="#eeeeee">
    <rect x="50" y="53" width="12" height="65"/><rect x="75" y="53" width="12" height="65"/><rect x="100" y="53" width="12" height="65"/><rect x="125" y="53" width="12" height="65"/><rect x="150" y="53" width="12" height="65"/>
    <rect x="175" y="53" width="12" height="65"/><rect x="200" y="53" width="12" height="65"/><rect x="225" y="53" width="12" height="65"/><rect x="250" y="53" width="12" height="65"/><rect x="275" y="53" width="12" height="65"/>
  </g>
  <rect x="50" y="61" width="12" height="57" fill="var(--green-soft)"/>
  <rect x="75" y="75" width="12" height="43" class="dot"/>
  <rect x="100" y="86" width="12" height="32" fill="var(--dark)"/>
  <rect x="125" y="74" width="12" height="44" class="dot"/>
  <rect x="150" y="55" width="12" height="63" fill="#c7cfd8"/>
  <rect x="175" y="64" width="12" height="54" fill="var(--green-soft)"/>
  <rect x="200" y="75" width="12" height="43" class="dot"/>
  <rect x="225" y="64" width="12" height="54" class="dot"/>
  <rect x="250" y="64" width="12" height="54" fill="var(--dark)"/>
  <rect x="275" y="55" width="12" height="63" class="dot"/>
  <g class="tiny mid"><text x="56" y="126">2001</text><text x="81" y="126">2002</text><text x="106" y="126">2003</text><text x="131" y="126">2004</text><text x="156" y="126">2005</text><text x="181" y="126">2006</text><text x="206" y="126">2007</text><text x="231" y="126">2008</text><text x="256" y="126">2009</text><text x="281" y="126">2010</text></g>
  <text x="22" y="166" class="foot">Business Presentation</text>
</svg></div>

<!-- 17 Data chart report -->
<div class="slide" style="left:434px;top:978px;width:311px;height:174px">
<svg viewBox="0 0 311 174">
  <circle cx="13" cy="16" r="3.5" class="dot"/><text x="19" y="18.5" class="logo">Brenthollow</text>
  <circle cx="285" cy="13" r="4" class="dot"/>
  <text x="156" y="13" class="sub">Insert your subtitle text here</text>
  <text x="156" y="26" class="ttl">Data Chart Report</text>
  <rect x="150" y="30" width="12" height="1" fill="var(--ink)"/>
  <g class="tiny end" style="font-size:2.8px"><text x="26" y="48">5</text><text x="26" y="59">4</text><text x="26" y="70">3</text><text x="26" y="81">2</text><text x="26" y="92">1</text><text x="26" y="103">0</text></g>
  <rect x="36" y="64" width="11" height="37" class="dot"/><rect x="48" y="69" width="11" height="32" fill="var(--green-soft)"/><rect x="60" y="56" width="11" height="45" fill="var(--dark)"/>
  <rect x="88" y="82" width="11" height="19" fill="var(--green-soft)"/><rect x="100" y="61" width="11" height="40" class="dot"/><rect x="112" y="70" width="11" height="31" fill="var(--dark)"/>
  <rect x="140" y="85" width="11" height="16" fill="var(--green-soft)"/><rect x="152" y="84" width="11" height="17" class="dot"/><rect x="164" y="70" width="11" height="31" fill="var(--dark)"/>
  <rect x="192" y="70" width="11" height="31" fill="var(--green-soft)"/><rect x="204" y="59" width="11" height="42" class="dot"/><rect x="216" y="70" width="11" height="31" fill="var(--dark)"/>
  <rect x="244" y="65" width="11" height="36" class="dot"/><rect x="256" y="67" width="11" height="34" fill="var(--green-soft)"/><rect x="268" y="56" width="11" height="45" fill="var(--dark)"/>
  <line x1="30" y1="101" x2="284" y2="101" stroke="var(--rule)" stroke-width=".5"/>
  <g class="tiny mid" style="font-size:2.8px"><text x="54" y="107">United States</text><text x="106" y="107">Canada</text><text x="158" y="107">Australia</text><text x="210" y="107">China</text><text x="262" y="107">Brazil</text></g>
  <rect x="134" y="113" width="14" height="4" class="dot"/><rect x="150" y="113" width="14" height="4" fill="var(--green-soft)"/><rect x="166" y="113" width="14" height="4" fill="var(--dark)"/>
  <text x="156" y="131" class="lbl mid">APP ANALYSIS</text>
  <text x="156" y="139" class="tiny mid">Mobile social media refers to the combination of mobile devices and social media. This is the group of mobile marketing applications that allow the creation.</text>
  <text x="156" y="144" class="tiny mid">Exchange of user generated content and media across many devices, networks and communities.</text>
  <text x="22" y="166" class="foot">Business Presentation</text>
</svg></div>

<!-- 18 Contact -->
<div class="slide" style="left:772px;top:978px;width:327px;height:180px">
<svg viewBox="0 0 327 180">
  <rect width="327" height="180" fill="#4f5a5f" role="img" aria-label="Team working around a table, seen from above, darkened"/>
  <text x="164" y="14" class="white-small mid">Insert your subtitle text here</text>
  <text x="164" y="27" class="mid" style="font-size:9.5px;font-weight:600;fill:#fff">Contact Us!</text>
  <rect x="158" y="31" width="12" height="1" fill="#fff"/>
  <path d="M36 81 q0 -4 3 -4 l2 3 -2 2 q1 3 4 4 l2 -2 3 2 q0 3 -4 3 q-8 -1 -8 -8z" fill="none" stroke="#fff" stroke-width=".7"/>
  <text x="44" y="82" class="white-small" style="fill:#fff;font-weight:600">Telephone</text>
  <text x="44" y="88" class="white-small" style="font-size:3px">Office: +1 555 0147 2210</text>
  <text x="44" y="93" class="white-small" style="font-size:3px">Mobile: +1 555 0183 6640</text>
  <path d="M140 78 a4 4 0 1 1 8 0 c0 3 -4 7 -4 7 c0 0 -4 -4 -4 -7z" fill="none" stroke="#fff" stroke-width=".7"/><circle cx="144" cy="78" r="1.2" fill="#fff"/>
  <text x="152" y="82" class="white-small" style="fill:#fff;font-weight:600">Location</text>
  <text x="152" y="88" class="white-small" style="font-size:3px">12 Harbor Lane, Suite 4</text>
  <text x="152" y="93" class="white-small" style="font-size:3px">Westmoor City</text>
  <circle cx="226" cy="81" r="4.5" fill="none" stroke="#fff" stroke-width=".7"/><ellipse cx="226" cy="81" rx="2" ry="4.5" fill="none" stroke="#fff" stroke-width=".5"/><line x1="221.5" y1="81" x2="230.5" y2="81" stroke="#fff" stroke-width=".5"/>
  <text x="235" y="82" class="white-small" style="fill:#fff;font-weight:600">Website</text>
  <text x="235" y="88" class="white-small" style="font-size:3px">www.brenthollow.example</text>
  <text x="235" y="93" class="white-small" style="font-size:3px">info@brenthollow.example</text>
</svg></div>

</body>
</html>
```